Business Cards + Letterhead for Software Development/Consulting Company
Practical Veltrane Orbis KPX Specialists
I need double sided standard sized Business Card [3.5" x 2"]
I like Segoe. Logo used in Logo is Fontin Sans
Professional
Torvald Ramsdal
President
2417 Quintara Ave
Glendale, CA 90871
torvald@ramsdal.example
I would not be opposed to use a special shape (http://cardmillvex.example/g/specialshape.do) especially the wink shape!
My printer have templates provided also: http://cardmillvex.example/g/showStaticPage.do?page=download_templates-bc.html
I envision a black background with the logo.
Logo (White Background) as received from Logo Contest Winner
Logo (Black Background) as received from Logo Contest Winner
Me - if you want to make a card with my picture on it

```html
<!DOCTYPE html>
<html lang="en">
<head>
<meta charset="utf-8">
<title>Ramsdal Consulting – Business Card</title>
<link rel="stylesheet" href="https://fonts.googleapis.com/css2?family=Open+Sans:wght@400;600;700&display=swap">
<style>
  :root {
    --stage: #1c1c1e;
    --card-white: #ffffff;
    --card-black: #141416;
    --band-tint: #1e2417;
    --ink: #1e1e20;
    --ink-soft: #555558;
    --paper-text: #f2f2f2;
    --green: #7cb83a;
    --orange: #f0a41e;
    --muted-white: #cfcfd2;
  }
  * { box-sizing: border-box; margin: 0; padding: 0; }
  html, body {
    width: 1200px; height: 871px; overflow: hidden;
    background: var(--stage);
    font-family: "Open Sans", sans-serif;
  }
  .stage {
    width: 1200px; height: 871px;
    display: flex; align-items: center; justify-content: center; gap: 40px;
  }
  .card {
    position: relative;
    width: 540px; height: 309px;
    overflow: hidden;
    border-radius: 3px;
    box-shadow: 0 10px 30px rgba(0,0,0,.5);
  }
  /* Front side */
  .card--front { background: var(--card-white); }
  .card__band {
    position: absolute; left: 0; right: 0; top: 176px; bottom: 0;
    background: linear-gradient(100deg, var(--card-black) 0%, var(--card-black) 55%, var(--band-tint) 100%);
  }
  .brand {
    position: absolute; top: 40px; right: 34px;
    display: flex; align-items: center; gap: 12px;
    color: var(--ink);
    font-weight: 600;
  }
  .brand__mark {
    width: 34px; height: 34px;
    background: var(--green);
  }
  .brand__name { line-height: 1; }
  .brand__name-main { display: block; font-size: 40px; letter-spacing: 1px; }
  .brand__name-sub { display: block; font-size: 19px; letter-spacing: 2px; margin-top: 4px; }
  .person {
    position: absolute; top: 122px; left: 300px;
    text-align: center; color: var(--ink);
  }
  .person__name { font-size: 14px; font-weight: 700; }
  .person__title { font-size: 11px; color: var(--ink-soft); }
  .contact {
    position: absolute; left: 22px; top: 196px;
    color: var(--paper-text);
    font-size: 9.5px; line-height: 1.45;
    list-style: none;
  }
  .contact__gap { height: 8px; }
  /* Back side */
  .card--back {
    background: linear-gradient(160deg, #2a2a2d 0%, var(--card-black) 55%, #0b0b0c 100%);
  }
  .tagline {
    position: absolute; top: 40px; right: 34px;
    color: var(--muted-white);
    font-size: 16px; font-weight: 600; letter-spacing: .5px;
  }
  .card--back .brand { top: auto; bottom: 70px; color: var(--paper-text); }
  .card--back .brand__mark { background: var(--orange); }
</style>
</head>
<body>
<main class="stage">
  <article class="card card--front" aria-label="Business card front">
    <div class="card__band" role="img" aria-label="Dark lower panel with a flowing green and orange swoosh decoration"></div>
    <div class="brand">
      <span class="brand__mark"></span>
      <span class="brand__name">
        <span class="brand__name-main">RAMSDAL</span>
        <span class="brand__name-sub">CONSULTING, INC.</span>
      </span>
    </div>
    <div class="person">
      <p class="person__name">Anders Velmo</p>
      <p class="person__title">Director</p>
    </div>
    <ul class="contact">
      <li>PO Box 7310, Quintara Heights</li>
      <li>CA 90871 USA</li>
      <li class="contact__gap"></li>
      <li>C. +1 (555) 014 2906</li>
      <li>E. anders.velmo@ramsdal.example</li>
      <li class="contact__gap"></li>
      <li>www.ramsdal.example</li>
    </ul>
  </article>

  <article class="card card--back" aria-label="Business card back">
    <p class="tagline">Commitment | Quality</p>
    <div class="brand">
      <span class="brand__mark"></span>
      <span class="brand__name">
        <span class="brand__name-main">RAMSDAL</span>
        <span class="brand__name-sub">CONSULTING, INC.</span>
      </span>
    </div>
  </article>
</main>
</body>
</html>
```